Revolutionary Video Platform (uncoded) - updated 05.11.

We want you to design the frontpage (uncoded) of FLIRTNOVA.net (we ev. hire the winner to create the subpages).

The concept of FLIRTNOVA.net is to show (ONLY!) infield videos of dating coaches (when they get in contact with women on the street) so that the users will have a solid base for deciding which coach they want to contact. I highlight that because some designs contained other ideas like "dating tips". No, we are specialized on infield videos. People should see if these coaches are really worth their money.

Therefore, the frontpage must include the following:

Header: Logo (attached), writing "FLIRTNOVA" or "FLIRT NOVA", links "Contact", "About", "Sign In", "Sign Up"

No design yet tried to change the logo in its size. You're welcome to do creative stuff.

What else is necessary on the front page:

1. 2 statements:

"Because 34 videos prove how to get every woman you want."
"Connect directly with 26 dating-coaches from these videos!"

The numbers should be showed in a way that the users know that they count up automatically; important: use the style zemlo has on it's front page by showing their amount of users.

2. Top rated Dating Coaches:

As the videos on the site can be rated, we want the coaches with the best rated videos on the front page with their faces (people can jump from there directly to their profiles).

To the pictures of the coaches you should also add the country flag and the city (where they come from). Plus, users should see who's on the first place, who's on the second place.. max. 10 coaches on the front page..

Set the title "TOP 10 DATING COACHES listed by best rated videos"

3. Search System

In order to find the videos the user is searching for, it needs a simple search form, where they can search after:

- Language
- Country
- City
- Rating
- Level of Difficulty
- Set-Size
- Conversation Starter

You can use simple white bars with a drop-down button.

4. Tags

Implement tags like "bitch shield, blow out opener, bounce, calibration, canned routine, challenge point, cockblock, cold approach, cold reading, compliment opener" etc.

Alphabetically listed..

5. Create previews of the (searched) videos which contains:

- Thumbnail of the video (only thumbnails on front page, no bigger video playback window, pls use pictures in order to make the site look more real)

- Some infos about the video (name of the coach with user-picture, duration, language, country (name and flag), city, audio comment (yes/no), difficulty level (super easy-expert), views, points needed to view (1-3), 5 star rating)

- Title and the beginning of the text about the video (written by the coach), i.e. about 30 words

- There are 2 sorts of videos.. (it's not necessary to explain why, it's just important that you implement two different versions of the video preview area (different only in terms of color!).. for example, some video preview areas could be edged in gold, others in silver.. or you could fill the whole video preview area with a color.. show me your taste... even though I prefer the more elegant way like gold and silver, you can probably surprise me with other color combinations..

- In order to simplify the process of comparing your designs, pls create 4 such preview video are areas..

6. Best voted video reviewer:

Users AND coaches will be able to write reviews about the videos. These reviews can be liked/voted. Therefore, we will know which user or coach writes the best reviews.

So we want you to implement also the charts of the 10 best voted video reviewers. Make sure there is a ranking list with the name of the user/coach and how many likes he got.
Here as well: add country flag, country and city (to see where they come from)..plus a little thumbnail of the profile picture.. Make sure the best 3 are being highlighted somehow..
Updates

Some designs were quite creative so far.
But unfortunately, less than half of the designers considered all requirements.
Therefore, be sure to implement all the requirements (for example, check new point nr. 6).
Without considering all the requirements, you don't have a chance to win this content.

Thank you.

Target Market(s)

male, 16-40 years old, worldwide audience

Industry/Entity Type

Dating

Requirements
Must have
• Not all submitted designs considered all requirements.

Therefore, please read the requirements carefully and consider all of them. If you want to add some new ideas or if you decide not to implement some requirements, I suggest to submit a second design.
Nice to have
• - if you have other ideas, feel free to add some of them to the front page, probably in form of a second design

- sometimes the same page will look totally different in other colors. Therefore, it would be great to add a 2nd version of your design, in terms of color

- the front page needs to be an eye-catcher

- different FLIRTNOVA font styles (come up with your own taste), a few different styles would be great!
Should not have
• - a search field like there is one in the first submitted design (the intelligent search is already being available with the filter system and the tags)

- female colors like pink/purple (it's a site only for men)

- a 08/15 look.. this will be the first website worldwide which contains videos from the best dating gurus on this planet in action.. they deserve a cool place to show their videos in order to gain new customers..

```html
<!DOCTYPE html>
<html lang="en">
<head>
<meta charset="utf-8">
<title>FLIRT NOVA – Infield Dating Videos</title>
<link href="https://fonts.googleapis.com/css2?family=Ubuntu:wght@400;500;700&family=Arimo:wght@400;700&display=swap" rel="stylesheet">
<style>
:root{
  --ink:#1d1d1d;
  --text:#333;
  --muted:#777;
  --line:#cfcfcf;
  --gold:#c9a10a;
  --gold-dark:#9c7a00;
  --gold-light:#e2bd2c;
  --hero:#a8a8a8;
  --hero-dark:#8e8e8e;
  --slate:#5b5b5b;
  --slate-dark:#3a3a3a;
  --panel:#eeeeee;
  --white:#fff;
}
*{box-sizing:border-box;margin:0;padding:0}
html,body{width:733px;height:1200px;overflow:hidden;background:var(--white);font-family:"Arimo",Arial,sans-serif;color:var(--text)}
.page{position:relative;width:733px;height:1200px}
.abs{position:absolute}

/* header */
.site-header{position:absolute;left:0;top:0;width:733px;height:68px;border-bottom:1px solid var(--line)}
.brand{position:absolute;left:104px;top:20px;display:flex;align-items:center;gap:6px;font-family:"Ubuntu",sans-serif;font-weight:700;font-size:13px;color:var(--ink);letter-spacing:.5px}
.brand-mark{width:14px;height:14px;background:var(--ink)}
.main-nav{position:absolute;top:12px;left:441px;display:flex;align-items:center;gap:0;font-size:8px;color:var(--ink)}
.main-nav a{color:inherit;text-decoration:none}
.nav-contact{position:absolute;left:0;top:3px}
.nav-about{position:absolute;left:42px;top:3px}
.btn-follow{position:absolute;left:73px;top:0;width:37px;height:13px;background:var(--gold);color:#fff;border-radius:2px;font-size:7.5px;line-height:13px;padding-left:5px}
.btn-signin{position:absolute;left:116px;top:0;width:36px;height:13px;background:var(--ink);color:#fff;border-radius:2px;font-size:7.5px;line-height:13px;text-align:center}
.nav-signup{position:absolute;left:161px;top:3px}
.social{position:absolute;left:553px;top:40px;display:flex;gap:3px}
.social span{width:10px;height:10px;border-radius:50%;background:#b5b5b5}

/* hero */
.hero{position:absolute;left:0;top:69px;width:733px;height:243px;background:var(--hero)}
.hero-figure{position:absolute;left:440px;top:0;width:220px;height:243px;background:linear-gradient(90deg,rgba(142,142,142,0) 0%,var(--hero-dark) 45%,#3b3b3b 80%)}
.hero-title{position:absolute;left:106px;top:30px;font-family:"Ubuntu",sans-serif;font-weight:500;font-size:25.5px;line-height:30px;color:#2b2b2b}
.counter{display:inline-flex;gap:4px;vertical-align:middle;margin:0 3px}
.counter b{display:inline-block;width:23px;height:31px;background:#1c1c1c;color:#fff;text-align:center;font-weight:400;font-size:20px;line-height:31px;border-radius:2px;border:1px solid #555}
.hero-sub{position:absolute;left:106px;top:134px;font-family:"Ubuntu",sans-serif;font-size:13px;color:var(--gold-dark);font-weight:500}
.hero-sub .counter b{width:19px;height:25px;font-size:15px;line-height:25px}

/* search */
.section-title{font-family:"Ubuntu",sans-serif;font-weight:500;color:#555}
.search-title{position:absolute;left:106px;top:328px;font-size:16px}
.search-box{position:absolute;left:106px;top:354px;width:520px;height:151px;border:1px solid #999;border-radius:3px;box-shadow:0 1px 3px rgba(0,0,0,.25)}
.field-label{position:absolute;font-size:9px;color:var(--ink);line-height:10px}
.select{position:absolute;width:115px;height:17px;border:1px solid #bbb;border-radius:2px;background:linear-gradient(#f7f7f7,#e3e3e3);font-size:7px;color:#aaa;line-height:15px;padding-left:9px}
.select::after{content:"";position:absolute;right:0;top:0;width:15px;height:15px;background:var(--slate)}
.select i{position:absolute;right:4px;top:3px;width:0;height:0;border-left:3.5px solid transparent;border-right:3.5px solid transparent;border-bottom:3.5px solid #fff;z-index:2}
.select i::after{content:"";position:absolute;left:-3.5px;top:5px;border-left:3.5px solid transparent;border-right:3.5px solid transparent;border-top:3.5px solid #fff}
.flag{display:inline-block;width:10px;height:7px;background:#233f8c;position:relative;vertical-align:middle}
.flag::before{content:"";position:absolute;left:4px;top:0;width:2px;height:7px;background:#d22}
.flag::after{content:"";position:absolute;left:0;top:2.5px;width:10px;height:2px;background:#d22}
.select .flag{position:absolute;right:22px;top:4px}
.slider{position:absolute;width:148px;height:8px;border-radius:4px;background:linear-gradient(#bdbdbd,#e0e0e0);border:1px solid #aaa}
.slider span{position:absolute;top:-2px;width:10px;height:10px;border-radius:50%;background:#fff;border:1px solid #888}
.slider span::after{content:"";position:absolute;left:3px;top:3px;width:2px;height:2px;border-radius:50%;background:#555}
.scale{position:absolute;font-size:7px;color:var(--ink)}
.btn-find{position:absolute;left:547px;top:474px;width:41px;height:18px;background:linear-gradient(var(--gold-light),var(--gold-dark));border-radius:2px;color:#fff;font-size:8px;font-weight:700;text-align:center;line-height:18px}

/* videos */
.video-grid{position:absolute;left:106px;top:522px;width:520px;height:314px;border:1px solid #aaa;border-top:2px solid var(--gold);border-radius:3px;box-shadow:0 1px 3px rgba(0,0,0,.25);overflow:hidden}
.video-card{position:absolute;width:258px;height:150px;font-size:6px;color:var(--ink);line-height:7.5px}
.video-card.premium{background:var(--panel)}
.uploader{position:absolute;left:13px;top:13px;display:flex;align-items:center;gap:6px}
.avatar{width:22px;height:22px;border:1px solid #aaa;background:#ddd;position:relative;overflow:hidden}
.avatar::before{content:"";position:absolute;left:6px;top:3px;width:9px;height:9px;border-radius:50%;background:#222}
.avatar::after{content:"";position:absolute;left:3px;top:13px;width:15px;height:12px;border-radius:7px 7px 0 0;background:#222}
.uploader b{font-weight:700}
.time{position:absolute;right:14px;top:21px;color:var(--muted)}
.thumb{position:absolute;left:13px;top:42px;width:120px;height:84px;border:2px solid #999;background:linear-gradient(135deg,#4f5a66,#9aa3ad 55%,#2e3540)}
.thumb.gold{border-color:var(--gold)}
.thumb.warm{background:linear-gradient(135deg,#d9d2c4,#8f6a48 55%,#52422f)}
.thumb.grey{background:linear-gradient(135deg,#e6e6e6,#9a9a9a 55%,#5c5c5c)}
.thumb.green{background:linear-gradient(135deg,#eef1e6,#7d8a5a 55%,#3d4a2a)}
.play{position:absolute;left:44px;top:27px;width:28px;height:26px;background:rgba(40,40,40,.75)}
.play::after{content:"";position:absolute;left:10px;top:6px;border-left:11px solid #fff;border-top:7px solid transparent;border-bottom:7px solid transparent}
.video-title{position:absolute;left:140px;top:42px;font-weight:700;font-size:7px}
.meta{position:absolute;left:140px;top:53px}
.meta-2{position:absolute;left:193px;top:53px}
.stars{position:absolute;left:140px;top:86px;color:var(--gold);font-size:8px;letter-spacing:-.5px}
.stars s{text-decoration:none;color:#bbb}
.audio{position:absolute;left:140px;top:99px;font-weight:700}
.audio em{font-style:normal;color:var(--gold)}
.excerpt{position:absolute;left:140px;top:107px;width:108px}
.pager{position:absolute;left:0;top:288px;width:518px;height:24px;font-size:7px;color:#444}
.pager .prev{position:absolute;left:14px;top:8px}
.pager .next{position:absolute;right:14px;top:8px}
.pager .pages{position:absolute;left:237px;top:4px;display:flex;gap:6px;align-items:center}
.pager .pages span{width:11px;text-align:center}
.pager .pages .current{width:13px;height:13px;border-radius:50%;border:1px solid #999;line-height:11px}

/* rankings */
.list-title{position:absolute;top:861px;font-size:11px;color:var(--ink)}
.rank-box{position:absolute;top:884px;width:172px;height:272px;border:1px solid #999;box-shadow:0 1px 3px rgba(0,0,0,.25)}
.rank-list{position:absolute;left:16px;top:10px;list-style:none}
.rank-list li{position:relative;width:142px;height:24px;margin-bottom:4px;border-radius:2px;background:linear-gradient(#6d6d6d,var(--slate-dark));border:1px solid #222;color:#fff;font-size:6.5px}
.rank-list li.top{background:linear-gradient(var(--gold-light),var(--gold-dark))}
.rank-list .pic{position:absolute;left:4px;top:3px;width:16px;height:16px;background:#2a2a2a;border:1px solid #888}
.rank-list .name{position:absolute;left:25px;top:3px;color:#eee}
.rank-list .loc{position:absolute;left:25px;top:13px;font-weight:700}
.rank-list .flag{width:8px;height:5px;margin:0 2px}
.rank-list .flag::before{left:3px;width:2px;height:5px}
.rank-list .flag::after{top:1.5px;width:8px;height:2px}
.rank-list .score{position:absolute;right:18px;top:6px;font-size:10px}
.rank-list .like{position:absolute;right:5px;top:7px;width:9px;height:9px}

/* tags */
.tag-box{position:absolute;left:486px;top:863px;width:143px;height:192px;border:1px solid #999;box-shadow:0 1px 3px rgba(0,0,0,.25)}
.tag-tab{position:absolute;left:91px;top:7px;width:34px;height:14px;background:#d9d9d9;border:1px solid #aaa;font-size:8px;line-height:12px;text-align:center;color:#666}
.tag-cloud{position:absolute;left:9px;top:29px;width:124px;height:146px;background:var(--panel);padding:10px 8px;font-size:8px;line-height:15px;color:#222}
.tag-cloud .xs{font-size:5px;color:#888}
.tag-cloud .s{font-size:6px}
.tag-cloud .l{font-size:14px}
.tag-cloud .m{font-size:11px}
.tag-cloud .soft{color:#999}

.site-footer{position:absolute;left:552px;top:1172px;display:flex;align-items:center;gap:6px}
.site-footer .brand-small{font-family:"Ubuntu",sans-serif;font-weight:700;font-size:6px;color:var(--ink)}
.site-footer small{font-size:6px;color:#444}
</style>
</head>
<body>
<div class="page">

  <header class="site-header">
    <div class="brand"><span class="brand-mark"></span>FLIRT NOVA</div>
    <nav class="main-nav">
      <a class="nav-contact" href="#">Contact</a>
      <a class="nav-about" href="#">About</a>
      <a class="btn-follow" href="#">Follow +</a>
      <a class="btn-signin" href="#">Sign In</a>
      <a class="nav-signup" href="#">Sign Up</a>
    </nav>
    <div class="social"><span></span><span></span><span></span><span></span><span></span></div>
  </header>

  <section class="hero">
    <div class="hero-figure" role="img" aria-label="Illustration of a caped hero silhouette with a heart on the chest"></div>
    <h1 class="hero-title">Because <span class="counter"><b>3</b><b>4</b></span> Videos show<br>how to get every woman<br>you want</h1>
    <p class="hero-sub">Connect directly with <span class="counter"><b>2</b><b>6</b></span> dating coaches worldwide</p>
  </section>

  <h2 class="section-title search-title">Advanced Video Search</h2>
  <form class="search-box">
    <span class="field-label" style="left:26px;top:17px">Language:</span>
    <span class="select" style="left:116px;top:12px">English<span class="flag"></span><i></i></span>
    <span class="field-label" style="left:26px;top:51px">Country:</span>
    <span class="select" style="left:116px;top:46px">UK<i></i></span>
    <span class="field-label" style="left:26px;top:85px">City:</span>
    <span class="select" style="left:116px;top:80px">London<i></i></span>
    <span class="field-label" style="left:26px;top:113px">Conversation<br>starter:</span>
    <span class="select" style="left:116px;top:114px">Undefined<i></i></span>

    <span class="field-label" style="left:258px;top:15px">Rating:</span>
    <span class="scale" style="left:344px;top:4px">1</span>
    <span class="scale" style="left:373px;top:4px">2</span>
    <span class="scale" style="left:403px;top:4px">3</span>
    <span class="scale" style="left:433px;top:4px">4</span>
    <span class="scale" style="left:462px;top:4px">5</span>
    <div class="slider" style="left:334px;top:17px"><span style="left:30px"></span><span style="left:136px"></span></div>

    <span class="field-label" style="left:258px;top:44px">Level of<br>difficulty:</span>
    <span class="scale" style="left:334px;top:41px">Super Easy</span>
    <span class="scale" style="left:393px;top:41px">Medium</span>
    <span class="scale" style="left:459px;top:41px">Expert</span>
    <div class="slider" style="left:334px;top:52px"><span style="left:30px"></span><span style="left:136px"></span></div>

    <span class="field-label" style="left:258px;top:85px">Set - size :</span>
    <span class="select" style="left:334px;top:80px;width:148px">Undefined<i></i></span>
  </form>
  <span class="btn-find">Find</span>

  <section class="video-grid">
    <article class="video-card" style="left:0;top:0">
      <div class="uploader"><span class="avatar"></span><span><b>Name Surname</b> uploaded a video</span></div>
      <span class="time">10 minutes ago</span>
      <div class="thumb" role="img" aria-label="Video thumbnail: coach talking on the street"><span class="play"></span></div>
      <div class="video-title">Jujubes jelly beans pastry</div>
      <div class="meta">Views: 65 650<br>Level: Super easy<br>Points: 3<br>10:45</div>
      <div class="meta-2">Language: English<br>UK <span class="flag"></span><br>London</div>
      <div class="stars">★★★<s>★★</s></div>
      <div class="audio">Audio comment: <em>Yes</em></div>
      <p class="excerpt">Jujubes jelly beans pastry cake biscuit jujubes oat cake. Candy canes candy canes topping lemon drops</p>
    </article>
    <article class="video-card premium" style="left:258px;top:0;width:262px">
      <div class="uploader"><span class="avatar"></span><span><b>Name Surname</b> uploaded a video</span></div>
      <span class="time">10 minutes ago</span>
      <div class="thumb gold warm" role="img" aria-label="Video thumbnail: coach chatting with a woman outdoors"><span class="play"></span></div>
      <div class="video-title">Jujubes jelly beans pastry</div>
      <div class="meta">Views: 65 650<br>Level: Super easy<br>Points: 3<br>10:45</div>
      <div class="meta-2">Language: English<br>UK <span class="flag"></span><br>London</div>
      <div class="stars">★★★<s>★★</s></div>
      <div class="audio">Audio comment: <em>Yes</em></div>
      <p class="excerpt">Jujubes jelly beans pastry cake biscuit jujubes oat cake. Candy canes candy canes topping lemon drops</p>
    </article>
    <article class="video-card" style="left:0;top:151px">
      <div class="uploader"><span class="avatar"></span><span><b>Name Surname</b> uploaded a video</span></div>
      <span class="time">10 minutes ago</span>
      <div class="thumb gold grey" role="img" aria-label="Video thumbnail: portrait of a coach"><span class="play"></span></div>
      <div class="video-title">Jujubes jelly beans pastry</div>
      <div class="meta">Views: 65 650<br>Level: Super easy<br>Points: 3<br>10:45</div>
      <div class="meta-2">Language: English<br>UK <span class="flag"></span><br>London</div>
      <div class="stars">★★★<s>★★</s></div>
      <div class="audio">Audio comment: <em>Yes</em></div>
      <p class="excerpt">Jujubes jelly beans pastry cake biscuit jujubes oat cake. Candy canes candy canes topping lemon drops</p>
    </article>
    <article class="video-card" style="left:258px;top:151px;width:262px">
      <div class="uploader"><span class="avatar"></span><span><b>Name Surname</b> uploaded a video</span></div>
      <span class="time">10 minutes ago</span>
      <div class="thumb green" role="img" aria-label="Video thumbnail: coach in a park"><span class="play"></span></div>
      <div class="video-title">Jujubes jelly beans pastry</div>
      <div class="meta">Views: 65 650<br>Level: Super easy<br>Points: 3<br>10:45</div>
      <div class="meta-2">Language: English<br>UK <span class="flag"></span><br>London</div>
      <div class="stars">★★★<s>★★</s></div>
      <div class="audio">Audio comment: <em>Yes</em></div>
      <p class="excerpt">Jujubes jelly beans pastry cake biscuit jujubes oat cake. Candy canes candy canes topping lemon drops</p>
    </article>
    <nav class="pager">
      <span class="prev">◀ &nbsp;Previous</span>
      <span class="pages"><span>1</span><span class="current">2</span><span>3</span></span>
      <span class="next">Next &nbsp;▶</span>
    </nav>
  </section>

  <h3 class="section-title list-title" style="left:104px">The 10 best voted video reviewers</h3>
  <div class="rank-box" style="left:104px">
    <ol class="rank-list">
      <li class="top"><span class="pic"></span><span class="name">Name Surname</span><span class="loc">UK<span class="flag"></span>London</span><span class="score">200</span><svg class="like" viewBox="0 0 10 10"><path d="M1 4h2v5H1zM4 4l2-3c1 0 1 1 1 2v1h2l-1 5H4z" fill="#fff"/></svg></li>
      <li class="top"><span class="pic"></span><span class="name">Name Surname</span><span class="loc">UK<span class="flag"></span>London</span><span class="score">200</span><svg class="like" viewBox="0 0 10 10"><path d="M1 4h2v5H1zM4 4l2-3c1 0 1 1 1 2v1h2l-1 5H4z" fill="#fff"/></svg></li>
      <li class="top"><span class="pic"></span><span class="name">Name Surname</span><span class="loc">UK<span class="flag"></span>London</span><span class="score">200</span><svg class="like" viewBox="0 0 10 10"><path d="M1 4h2v5H1zM4 4l2-3c1 0 1 1 1 2v1h2l-1 5H4z" fill="#fff"/></svg></li>
      <li><span class="pic"></span><span class="name">Name Surname</span><span class="loc">UK<span class="flag"></span>London</span><span class="score">200</span><svg class="like" viewBox="0 0 10 10"><path d="M1 4h2v5H1zM4 4l2-3c1 0 1 1 1 2v1h2l-1 5H4z" fill="#fff"/></svg></li>
      <li><span class="pic"></span><span class="name">Name Surname</span><span class="loc">UK<span class="flag"></span>London</span><span class="score">200</span><svg class="like" viewBox="0 0 10 10"><path d="M1 4h2v5H1zM4 4l2-3c1 0 1 1 1 2v1h2l-1 5H4z" fill="#fff"/></svg></li>
      <li><span class="pic"></span><span class="name">Name Surname</span><span class="loc">UK<span class="flag"></span>London</span><span class="score">200</span><svg class="like" viewBox="0 0 10 10"><path d="M1 4h2v5H1zM4 4l2-3c1 0 1 1 1 2v1h2l-1 5H4z" fill="#fff"/></svg></li>
      <li><span class="pic"></span><span class="name">Name Surname</span><span class="loc">UK<span class="flag"></span>London</span><span class="score">200</span><svg class="like" viewBox="0 0 10 10"><path d="M1 4h2v5H1zM4 4l2-3c1 0 1 1 1 2v1h2l-1 5H4z" fill="#fff"/></svg></li>
      <li><span class="pic"></span><span class="name">Name Surname</span><span class="loc">UK<span class="flag"></span>London</span><span class="score">200</span><svg class="like" viewBox="0 0 10 10"><path d="M1 4h2v5H1zM4 4l2-3c1 0 1 1 1 2v1h2l-1 5H4z" fill="#fff"/></svg></li>
      <li><span class="pic"></span><span class="name">Name Surname</span><span class="loc">UK<span class="flag"></span>London</span><span class="score">200</span><svg class="like" viewBox="0 0 10 10"><path d="M1 4h2v5H1zM4 4l2-3c1 0 1 1 1 2v1h2l-1 5H4z" fill="#fff"/></svg></li>
    </ol>
  </div>

  <h3 class="section-title list-title" style="left:295px">The 10 best voted video coaches</h3>
  <div class="rank-box" style="left:295px">
    <ol class="rank-list">
      <li class="top"><span class="pic"></span><span class="name">Name Surname</span><span class="loc">UK<span class="flag"></span>London</span><span class="score">200</span><svg class="like" viewBox="0 0 10 10"><path d="M1 4h2v5H1zM4 4l2-3c1 0 1 1 1 2v1h2l-1 5H4z" fill="#fff"/></svg></li>
      <li class="top"><span class="pic"></span><span class="name">Name Surname</span><span class="loc">UK<span class="flag"></span>London</span><span class="score">200</span><svg class="like" viewBox="0 0 10 10"><path d="M1 4h2v5H1zM4 4l2-3c1 0 1 1 1 2v1h2l-1 5H4z" fill="#fff"/></svg></li>
      <li class="top"><span class="pic"></span><span class="name">Name Surname</span><span class="loc">UK<span class="flag"></span>London</span><span class="score">200</span><svg class="like" viewBox="0 0 10 10"><path d="M1 4h2v5H1zM4 4l2-3c1 0 1 1 1 2v1h2l-1 5H4z" fill="#fff"/></svg></li>
      <li><span class="pic"></span><span class="name">Name Surname</span><span class="loc">UK<span class="flag"></span>London</span><span class="score">200</span><svg class="like" viewBox="0 0 10 10"><path d="M1 4h2v5H1zM4 4l2-3c1 0 1 1 1 2v1h2l-1 5H4z" fill="#fff"/></svg></li>
      <li><span class="pic"></span><span class="name">Name Surname</span><span class="loc">UK<span class="flag"></span>London</span><span class="score">200</span><svg class="like" viewBox="0 0 10 10"><path d="M1 4h2v5H1zM4 4l2-3c1 0 1 1 1 2v1h2l-1 5H4z" fill="#fff"/></svg></li>
      <li><span class="pic"></span><span class="name">Name Surname</span><span class="loc">UK<span class="flag"></span>London</span><span class="score">200</span><svg class="like" viewBox="0 0 10 10"><path d="M1 4h2v5H1zM4 4l2-3c1 0 1 1 1 2v1h2l-1 5H4z" fill="#fff"/></svg></li>
      <li><span class="pic"></span><span class="name">Name Surname</span><span class="loc">UK<span class="flag"></span>London</span><span class="score">200</span><svg class="like" viewBox="0 0 10 10"><path d="M1 4h2v5H1zM4 4l2-3c1 0 1 1 1 2v1h2l-1 5H4z" fill="#fff"/></svg></li>
      <li><span class="pic"></span><span class="name">Name Surname</span><span class="loc">UK<span class="flag"></span>London</span><span class="score">200</span><svg class="like" viewBox="0 0 10 10"><path d="M1 4h2v5H1zM4 4l2-3c1 0 1 1 1 2v1h2l-1 5H4z" fill="#fff"/></svg></li>
      <li><span class="pic"></span><span class="name">Name Surname</span><span class="loc">UK<span class="flag"></span>London</span><span class="score">200</span><svg class="like" viewBox="0 0 10 10"><path d="M1 4h2v5H1zM4 4l2-3c1 0 1 1 1 2v1h2l-1 5H4z" fill="#fff"/></svg></li>
    </ol>
  </div>

  <aside class="tag-box">
    <span class="tag-tab">Tags</span>
    <div class="tag-cloud">
      <span class="xs">bitch shield,</span> <span class="s">blow out opener, bounce,</span><br>
      <span class="s">calibration,</span> <span class="xs">canned routine,</span><br>
      <span class="l">challenge point,</span><br>
      <span class="xs">cockblock,</span> <span class="m">cold approach,</span><br>
      <span class="xs">cold reading,</span> <span class="m soft">compliment opener,</span><br>
      <span class="m">cold approach,</span><br>
      <span class="xs">cold reading,</span> <span class="m soft">compliment</span>
    </div>
  </aside>

  <footer class="site-footer">
    <span class="brand-small">FLIRT NOVA</span>
    <small>Copyright 2012</small>
  </footer>

</div>
</body>
</html>
```